Presentation & Communication (Guide, Ebook, carroussel vistelle, corvanet et plumora)

Suite à la conception du logo, je souhaite désormais développer une identité visuelle complète ainsi que des supports marketing pour ma page Plumora, ma communication client interne notamment :
- Couverture Plumora + Photo de profil Plumora
- Guides
- E-books
- Et enfin, une charte graphique destinée aux formulaires sous format Microsoft Forms (pour la collecte de sondages et la prospection).
Vous trouverez ci-joint le logo que vous avez créé, ainsi qu’une couverture que j’ai réalisée via Canva. Cependant, lors de l’importation sur Plumora, le logo et les illustrations apparaissent flous.
Rappel important :
La direction artistique et l’identité visuelle doivent être en parfaite cohérence avec le logo et l’activité, à savoir :
un cabinet d’expertise comptable spécialisé pour les chirurgiens-dentistes et les centres dentaires. Je souhaite quelque chose de minimaliste, haut de gamme et moderne (je veux pas des logos de dents et d'instrument grossier et dans tous les sens).
Les couleurs qui ont été utilisées pour le site sont principalement : #0F1121 ; #FFFFFF ; #4A90A4 ; #5FAFB3.
Les supports doivent être téléchargeable sous format pack office de façon à pouvoir les utiliser et rédiger dessus du texte (guides, e-books, image pour post réseaux sociaux). Il faut donc déterminer une police efficace qui correspond à l'image de mon cabinet comptable (Poppins peut être ?)
Ce que j'aimerais :
1) Une visuel de page de couverture Plu mora
2) Un visuel d'image de profil (Icône) de page Plumora / Vistelle de mon logo
3) Un visuel moderne, haut de gamme et élégant au bon format en utilsant en partie les couleurs évoqué dans le brief. Ce visuel doit être adaptée au format Post publication Vistelle et Plumora avec un visuel autour mais avec la possibilité d'écrire du texte sur le support que vous créér (exemple pièce jointe d'un confrère à moi)
4) Un support Guide de façon également à rédiger dessus simplement avec une bonne typographie moderne et professionnelle, sur plusieurs pages à minima sur 10 pages. Je demande un peu la création d'un thème sous format pack office pour simplifier l'utilisation du fichier et le process pour uniquement éditer et importer sur CorvaNet, Plumora et Vistelle sans transformer ou redymensionner ou rogner la qualité du support. (Deux Exemples ci-joint).
5) Créer un Ebook de la même manière avec un fond (un thème) qui représente bien mon cabinet haut de gamme, classe et moderne. (Exemple Ebook ci-joint)
English :
Following the logo design, I now wish to develop a complete visual identity and marketing materials for my Plumora page and internal client communications, including:
- Plumora cover photo + Plumora profile picture
- Guides
- E-books
- And finally, a style guide for Microsoft Forms forms (for survey collection and lead generation).
Attached you will find the logo you created, as well as a cover photo I designed using Canva. However, when uploaded to Plumora, the logo and illustrations appear blurry.
Important reminder:
The art direction and visual identity must be perfectly consistent with the logo and the business activity, namely:
an accounting firm specializing in services for dentists and dental clinics. I want something minimalist, high-end, and modern (I don't want logos of teeth and crude instruments in all directions).
The colors used for the website are primarily: #0F1121; #FFFFFF; #4A90A4; #5FAFB3.
The materials must be downloadable in Microsoft Office format so they can be used and text added to (guides, e-books, images for social media posts). Therefore, an effective font that matches my accounting firm's image needs to be chosen (Poppins, perhaps?).
What I would like:
1) A Plumora cover image
2) A Plumora/Vistelle profile picture (icon) of my logo
3) A modern, high-end, and elegant image in the correct format, partially using the colors mentioned in the brief. This image must be suitable for Vistelle and Plumora posts, with a surrounding image, but with the option to write text on the document you create (example attached from a colleague).
4) A guide template, also easy to write on, with good, modern, and professional typography, spanning at least 10 pages. I would like a template created in Microsoft Office format to simplify file use and the process of simply editing and importing it to CorvaNet, Plumora, and Vistelle without transforming, resizing, or cropping the document. (Two examples attached).
5) Create an ebook in the same style with a background (theme) that accurately represents my high-end, classy, and modern firm. (Example ebook attached)
Chirurgiens dentistes, orthodontistes
Expertise comptable et conseil fiscal

```html
<!DOCTYPE html>
<html lang="en">
<head>
<meta charset="utf-8">
<title>Velnor Identity Design</title>
<link rel="stylesheet" href="https://fonts.googleapis.com/css2?family=Montserrat:wght@300;400;500;600;800&display=swap">
<style>
  :root {
    --navy: #2b2a5e;
    --navy-deep: #141530;
    --navy-mid: #25226a;
    --violet: #4a4790;
    --violet-text: #4a46a8;
    --ink: #0f1121;
    --cream: #e3dcc8;
    --cream-light: #e8e1ce;
    --lavender: #eeeefc;
    --white: #ffffff;
    --gray: #dedede;
    --skin: #c9a68a;
    --coat: #2a2a30;
  }
  * { box-sizing: border-box; margin: 0; padding: 0; }
  html, body { width: 1200px; height: 2638px; overflow: hidden; }
  body {
    position: relative;
    font-family: "Montserrat", sans-serif;
    background:
      radial-gradient(ellipse 700px 500px at 80% 30%, rgba(255,255,255,.95), rgba(255,255,255,0)),
      radial-gradient(ellipse 800px 700px at 30% 75%, rgba(255,255,255,.7), rgba(255,255,255,0)),
      linear-gradient(180deg, #f2f2f2 0%, var(--gray) 55%, #f4f4f4 100%);
  }
  .page-header {
    position: absolute; left: 0; top: 0; width: 1200px; height: 205px;
    background: var(--navy);
    box-shadow: 0 8px 24px rgba(0,0,0,.18);
    display: flex; align-items: center; justify-content: center;
  }
  .page-title {
    color: var(--cream-light); font-weight: 300; font-size: 68px; letter-spacing: 2px;
  }
  .section-label {
    position: absolute; left: 128px; font-weight: 300; font-size: 40px; color: #2a2a2a;
  }
  .section-label.profile { top: 290px; }
  .section-label.social { top: 693px; }

  .avatar {
    position: absolute; top: 366px; width: 216px; height: 216px; border-radius: 50%;
    display: flex; align-items: center; justify-content: center;
    font-weight: 600; font-size: 36px;
  }
  .avatar.dark { left: 121px; background: var(--ink); color: var(--cream); }
  .avatar.cream { left: 368px; background: var(--cream); color: var(--ink); border: 6px solid var(--white); }
  .avatar.light { left: 618px; background: var(--white); color: var(--navy-mid); border: 3px solid var(--cream); }
  .avatar.violet { left: 862px; background: var(--navy-mid); color: var(--white); }

  .cover { position: absolute; width: 440px; height: 550px; display: block; }
  .cover.col-a { left: 133px; }
  .cover.col-b { left: 634px; }
  .cover.row-1 { top: 768px; }
  .cover.row-2 { top: 1357px; }
  .cover.row-3 { top: 1954px; }

  .headline { font-family: "Montserrat", sans-serif; font-weight: 800; }
  .subline { font-family: "Montserrat", sans-serif; font-weight: 300; }
  .box-title { font-family: "Montserrat", sans-serif; font-weight: 500; font-size: 13px; }
  .box-body { font-family: "Montserrat", sans-serif; font-weight: 300; font-size: 9.6px; }
  .url { font-family: "Montserrat", sans-serif; font-weight: 400; font-size: 8.5px; fill: #333; }
  .brand-mini { font-family: "Montserrat", sans-serif; font-weight: 600; font-size: 11px; }
</style>
</head>
<body>

<header class="page-header">
  <h1 class="page-title">VELNOR IDENTITY DESIGN</h1>
</header>

<h2 class="section-label profile">Profile:</h2>
<div class="avatar dark">Velnor</div>
<div class="avatar cream">Velnor</div>
<div class="avatar light">Velnor</div>
<div class="avatar violet">Velnor</div>

<h2 class="section-label social">Social Media Cover:</h2>

<!-- Cover 1: handshake, arch -->
<svg class="cover col-a row-1" viewBox="0 0 430 537">
  <defs>
    <linearGradient id="c1-bg" x1="0" y1="0" x2="1" y2="1"><stop offset="0" stop-color="#12122a"/><stop offset="1" stop-color="#1d1c45"/></linearGradient>
    <radialGradient id="c1-arch" cx=".5" cy=".3" r=".7"><stop offset="0" stop-color="#5e5890"/><stop offset="1" stop-color="#3c3880"/></radialGradient>
    <linearGradient id="c1-photo" x1="0" x2="1"><stop offset="0" stop-color="#1c1c2c"/><stop offset=".4" stop-color="#c9a68a"/><stop offset=".6" stop-color="#d6b79c"/><stop offset="1" stop-color="#1f2238"/></linearGradient>
  </defs>
  <rect width="430" height="537" fill="url(#c1-bg)"/>
  <path d="M85,537 L85,165 A130,130 0 0 1 345,165 L345,537 Z" fill="url(#c1-arch)"/>
  <rect role="img" aria-label="Photo of two people in dark suits shaking hands" x="0" y="140" width="430" height="175" rx="60" fill="url(#c1-photo)" opacity=".85"/>
  <path d="M0,275 C40,380 120,420 215,405 C300,392 360,372 430,372 L430,537 L0,537 Z" fill="var(--cream)"/>
  <circle cx="24" cy="36" r="9" fill="none" stroke="var(--cream)" stroke-width="2"/>
  <text class="brand-mini" x="38" y="40" fill="var(--cream)">Velnor</text>
  <text class="headline" x="215" y="453" font-size="40" text-anchor="middle" fill="var(--ink)">Your text</text>
  <text class="subline" x="215" y="489" font-size="29" text-anchor="middle" fill="var(--ink)">will be placed here.</text>
  <rect x="298" y="511" width="132" height="14" rx="3" fill="var(--white)"/>
  <circle cx="307" cy="518" r="6" fill="var(--navy-mid)"/>
  <text class="url" x="318" y="521">www.velnorexpertise.fr</text>
</svg>

<!-- Cover 2: portrait, arch -->
<svg class="cover col-b row-1" viewBox="0 0 430 537">
  <defs>
    <linearGradient id="c2-bg" x1="0" y1="0" x2="1" y2="1"><stop offset="0" stop-color="#12122a"/><stop offset="1" stop-color="#1d1c45"/></linearGradient>
    <radialGradient id="c2-arch" cx=".5" cy=".3" r=".7"><stop offset="0" stop-color="#5e5890"/><stop offset="1" stop-color="#3c3880"/></radialGradient>
    <linearGradient id="c2-photo" x1="0" y1="0" x2="0" y2="1"><stop offset="0" stop-color="#5a4a42"/><stop offset=".3" stop-color="#2e2d33"/><stop offset="1" stop-color="#1e1e24"/></linearGradient>
  </defs>
  <rect width="430" height="537" fill="url(#c2-bg)"/>
  <path d="M85,537 L85,165 A130,130 0 0 1 345,165 L345,537 Z" fill="url(#c2-arch)"/>
  <rect role="img" aria-label="Photo of a bearded man in a dark coat writing in a notebook" x="65" y="40" width="315" height="370" rx="40" fill="url(#c2-photo)"/>
  <path d="M0,275 C40,380 120,420 215,405 C300,392 360,372 430,372 L430,537 L0,537 Z" fill="var(--cream)"/>
  <circle cx="24" cy="36" r="9" fill="none" stroke="var(--cream)" stroke-width="2"/>
  <text class="brand-mini" x="38" y="40" fill="var(--cream)">Velnor</text>
  <text class="headline" x="215" y="453" font-size="40" text-anchor="middle" fill="var(--ink)">Your text</text>
  <text class="subline" x="215" y="489" font-size="29" text-anchor="middle" fill="var(--ink)">will be placed here.</text>
  <rect x="298" y="511" width="132" height="14" rx="3" fill="var(--white)"/>
  <circle cx="307" cy="518" r="6" fill="var(--navy-mid)"/>
  <text class="url" x="318" y="521">www.velnorexpertise.fr</text>
</svg>

<!-- Cover 3: portrait left, text right -->
<svg class="cover col-a row-2" viewBox="0 0 430 537">
  <defs>
    <linearGradient id="c3-bg" x1="0" y1="0" x2="0" y2="1"><stop offset="0" stop-color="#3a3a8a"/><stop offset=".55" stop-color="#1e1d4e"/><stop offset="1" stop-color="#131330"/></linearGradient>
    <linearGradient id="c3-photo" x1="0" y1="0" x2="0" y2="1"><stop offset="0" stop-color="#5a4a42"/><stop offset=".3" stop-color="#2e2d33"/><stop offset="1" stop-color="#1e1e24"/></linearGradient>
  </defs>
  <rect width="430" height="537" fill="url(#c3-bg)"/>
  <path d="M0,35 L175,35 A40,40 0 0 1 215,75 L215,537 L0,537 Z" fill="var(--lavender)"/>
  <rect role="img" aria-label="Photo of a bearded man in a dark coat writing in a notebook" x="10" y="55" width="350" height="330" rx="30" fill="url(#c3-photo)"/>
  <circle cx="392" cy="35" r="18" fill="var(--white)"/>
  <text class="brand-mini" x="392" y="39" font-size="9" text-anchor="middle" fill="var(--navy-mid)">Velnor</text>
  <text class="headline" x="232" y="220" font-size="33" fill="var(--white)">Your text</text>
  <text class="subline" x="232" y="243" font-size="20" fill="var(--white)">will be</text>
  <text class="subline" x="232" y="267" font-size="20" fill="var(--white)">placed here.</text>
  <path d="M0,385 L360,385 A48,48 0 0 1 360,482 L0,482 Z" fill="var(--cream)"/>
  <rect x="36" y="395" width="6" height="6" fill="var(--navy-mid)"/>
  <text class="box-title" x="51" y="403" fill="var(--ink)">What is Lorem Ipsum?</text>
  <g class="box-body" fill="#2a2a2a">
    <text x="36" y="419">Lorem Ipsum is simply dummy text of the printing and typesetting</text>
    <text x="36" y="431">industry. Lorem Ipsum has been the industry's standard dummy</text>
    <text x="36" y="443">text ever since the 1500s, when an unknown printer took a galley of</text>
    <text x="36" y="455">type and scrambled it to make a type specimen book. It has</text>
    <text x="36" y="467">survived not only five centuries, but also</text>
  </g>
  <rect x="298" y="504" width="132" height="14" rx="3" fill="var(--white)"/>
  <circle cx="307" cy="511" r="6" fill="var(--navy-mid)"/>
  <text class="url" x="318" y="514">www.velnorexpertise.fr</text>
</svg>

<!-- Cover 4: light arch panel with handshake -->
<svg class="cover col-b row-2" viewBox="0 0 430 537">
  <defs>
    <linearGradient id="c4-bg" x1="1" y1="0" x2="0" y2="1"><stop offset="0" stop-color="#3a3a8a"/><stop offset=".6" stop-color="#1d1c48"/><stop offset="1" stop-color="#131330"/></linearGradient>
    <linearGradient id="c4-photo" x1="0" x2="1"><stop offset="0" stop-color="#1c1c2c"/><stop offset=".4" stop-color="#c9a68a"/><stop offset=".6" stop-color="#d6b79c"/><stop offset="1" stop-color="#1f2238"/></linearGradient>
  </defs>
  <rect width="430" height="537" fill="url(#c4-bg)"/>
  <path d="M32,537 L32,145 A110,110 0 0 1 142,35 L290,35 A110,110 0 0 1 400,145 L400,537 Z" fill="var(--lavender)"/>
  <rect role="img" aria-label="Photo of two people in dark suits shaking hands" x="0" y="190" width="430" height="170" rx="50" fill="url(#c4-photo)" opacity=".85"/>
  <path d="M0,497 A40,40 0 0 1 40,537 L0,537 Z" fill="var(--cream)"/>
  <path d="M430,497 A40,40 0 0 0 390,537 L430,537 Z" fill="var(--cream)"/>
  <circle cx="225" cy="35" r="20" fill="var(--white)"/>
  <text class="brand-mini" x="225" y="39" font-size="9" text-anchor="middle" fill="var(--navy-mid)">Velnor</text>
  <text class="headline" x="215" y="108" font-size="38" text-anchor="middle" fill="var(--ink)">Your text</text>
  <text class="subline" x="215" y="144" font-size="27" text-anchor="middle" fill="var(--violet-text)">will be placed here.</text>
  <rect x="88" y="380" width="267" height="98" rx="20" fill="var(--cream)"/>
  <rect x="102" y="390" width="6" height="6" fill="var(--navy-mid)"/>
  <text class="box-title" x="117" y="398" fill="var(--ink)">What is Lorem Ipsum?</text>
  <g class="box-body" fill="#2a2a2a" font-size="8.6">
    <text x="102" y="413">Lorem Ipsum is simply dummy text of the printing and</text>
    <text x="102" y="424">typesetting industry. Lorem Ipsum has been the</text>
    <text x="102" y="435">industry's standard dummy text ever since the 1500s,</text>
    <text x="102" y="446">when an unknown printer took a galley of type and</text>
    <text x="102" y="457">scrambled it to make a type specimen book. It has</text>
    <text x="102" y="468">survived not only five centuries, but also</text>
  </g>
  <rect x="148" y="504" width="132" height="14" rx="3" fill="var(--white)"/>
  <circle cx="157" cy="511" r="6" fill="var(--navy-mid)"/>
  <text class="url" x="168" y="514">www.velnorexpertise.fr</text>
</svg>

<!-- Cover 5: text top, navy handshake panel -->
<svg class="cover col-a row-3" viewBox="0 0 430 537">
  <defs>
    <linearGradient id="c5-bg" x1="0" y1="0" x2="0" y2="1"><stop offset="0" stop-color="#e6e6f6"/><stop offset="1" stop-color="#ffffff"/></linearGradient>
    <linearGradient id="c5-photo" x1="0" x2="1"><stop offset="0" stop-color="#1c1c2c"/><stop offset=".4" stop-color="#c9a68a"/><stop offset=".6" stop-color="#d6b79c"/><stop offset="1" stop-color="#1f2238"/></linearGradient>
  </defs>
  <rect width="430" height="537" fill="url(#c5-bg)"/>
  <path d="M180,0 L430,0 L430,150 C360,90 280,30 180,0 Z" fill="var(--cream)"/>
  <circle cx="380" cy="35" r="9" fill="none" stroke="var(--violet-text)" stroke-width="2"/>
  <text class="brand-mini" x="372" y="62" font-size="9" fill="var(--violet-text)">Velnor</text>
  <text class="headline" x="36" y="68" font-size="33" fill="var(--navy-mid)">Your text</text>
  <text class="subline" x="36" y="106" font-size="29" fill="var(--navy-mid)">will be</text>
  <text class="subline" x="36" y="140" font-size="29" fill="var(--navy-mid)">placed here.</text>
  <path d="M73,175 L430,175 L430,380 L73,380 A40,40 0 0 1 33,340 L33,215 A40,40 0 0 1 73,175 Z" fill="var(--navy-mid)"/>
  <rect role="img" aria-label="Photo of two people in dark suits shaking hands" x="0" y="190" width="430" height="160" rx="50" fill="url(#c5-photo)" opacity=".8"/>
  <rect x="36" y="403" width="6" height="6" fill="var(--navy-mid)"/>
  <text class="box-title" x="51" y="411" fill="var(--ink)">What is Lorem Ipsum?</text>
  <g class="box-body" fill="#2a2a2a">
    <text x="36" y="427">Lorem Ipsum is simply dummy text of the printing and typesetting</text>
    <text x="36" y="439">industry. Lorem Ipsum has been the industry's standard dummy</text>
    <text x="36" y="451">text ever since the 1500s, when an unknown printer took a galley of</text>
    <text x="36" y="463">type and scrambled it to make a type specimen book. It has</text>
    <text x="36" y="475">survived not only five centuries, but also</text>
  </g>
  <rect x="36" y="504" width="132" height="14" rx="7" fill="var(--cream)"/>
  <circle cx="45" cy="511" r="6" fill="var(--navy-mid)"/>
  <text class="url" x="56" y="514">www.velnorexpertise.fr</text>
</svg>

<!-- Cover 6: navy header band, portrait -->
<svg class="cover col-b row-3" viewBox="0 0 430 537">
  <defs>
    <linearGradient id="c6-bg" x1="0" y1="0" x2="0" y2="1"><stop offset="0" stop-color="#e6e6f6"/><stop offset="1" stop-color="#ffffff"/></linearGradient>
    <linearGradient id="c6-photo" x1="0" y1="0" x2="0" y2="1"><stop offset="0" stop-color="#5a4a42"/><stop offset=".3" stop-color="#2e2d33"/><stop offset="1" stop-color="#1e1e24"/></linearGradient>
  </defs>
  <rect width="430" height="537" fill="url(#c6-bg)"/>
  <rect width="430" height="150" fill="var(--navy-mid)"/>
  <circle cx="383" cy="35" r="9" fill="none" stroke="var(--white)" stroke-width="2"/>
  <text class="brand-mini" x="374" y="60" font-size="9" fill="var(--white)">Velnor</text>
  <text class="headline" x="38" y="64" font-size="38" fill="var(--white)">Your text</text>
  <text class="subline" x="38" y="106" font-size="31" fill="var(--white)">will be placed here.</text>
  <rect x="148" y="143" width="132" height="14" rx="7" fill="var(--cream)"/>
  <circle cx="157" cy="150" r="6" fill="var(--navy-mid)"/>
  <text class="url" x="168" y="153">www.velnorexpertise.fr</text>
  <rect role="img" aria-label="Photo of a bearded man in a dark coat writing in a notebook" x="65" y="172" width="315" height="300" rx="30" fill="url(#c6-photo)"/>
  <path d="M65,537 L65,498 A30,30 0 0 1 95,468 L338,468 A30,30 0 0 1 368,498 L368,537 Z" fill="var(--cream)"/>
  <rect x="84" y="482" width="6" height="6" fill="var(--navy-mid)"/>
  <text class="box-title" x="99" y="490" fill="var(--ink)">What is Lorem Ipsum?</text>
  <g class="box-body" fill="#2a2a2a" font-size="9">
    <text x="84" y="505">Lorem Ipsum is simply dummy text of the printing and</text>
    <text x="84" y="517">typesetting industry. Lorem Ipsum has been the</text>
  </g>
</svg>

</body>
</html>
```